Willowbend Pharmacy Business Cards

I need a business card design and or template. Needs to convey a softer feel along with health and wellness. Please see attached logo and color scheme.

Industry/Entity Type

Pharmacy

Colors

Designer to choose colors to be used in the design.

Requirements
Must have
• I've added a second NEW colored logo I think I am going to go with the blue green logo.
• Needs to have the colors and feel of the logo attached.
• Darrel Quimby
• Pharmacy Manager
• willowbendpharmacy.example

```html
<!DOCTYPE html>
<html lang="en">
<head>
<meta charset="utf-8">
<title>Willowbend Pharmacy – Business Cards</title>
<link rel="stylesheet" href="https://fonts.googleapis.com/css2?family=Lato:wght@400;700&display=swap">
<style>
  :root {
    --backdrop: #676767;
    --card-white: #ffffff;
    --teal-top: #3e9bb2;
    --green-bottom: #9cc653;
    --brand-blue: #2fa5dc;
    --brand-grey: #5c5e61;
    --ink: #2b2b2b;
    --on-colour: #ffffff;
  }
  * { margin: 0; padding: 0; box-sizing: border-box; }
  html, body { width: 1200px; height: 802px; overflow: hidden; }
  body {
    background: var(--backdrop);
    font-family: "Lato", sans-serif;
    position: relative;
  }
  .card {
    position: absolute;
    top: 274px;
    width: 443px;
    height: 265px;
  }
  .card--front {
    left: 136px;
    background: linear-gradient(180deg, var(--teal-top) 0%, #6db08a 50%, var(--green-bottom) 100%);
    color: var(--on-colour);
  }
  .card--back {
    left: 624px;
    background: var(--card-white);
  }
  .holder {
    position: absolute;
    right: 30px;
    top: 113px;
    text-align: right;
  }
  .holder__name {
    font-weight: 700;
    font-size: 16px;
    letter-spacing: 0.2px;
    line-height: 1.15;
  }
  .holder__role {
    font-size: 12.5px;
    line-height: 1.2;
  }
  .contact {
    position: absolute;
    right: 30px;
    top: 178px;
    list-style: none;
    font-size: 12.5px;
    line-height: 16px;
    text-align: right;
  }
  .contact li {
    display: flex;
    justify-content: flex-end;
    align-items: center;
    gap: 4px;
  }
  .contact svg { width: 10px; height: 10px; fill: var(--on-colour); }
  .brand {
    position: absolute;
    left: 0;
    right: 0;
    top: 108px;
    display: flex;
    justify-content: center;
    align-items: center;
    gap: 10px;
  }
  .brand__dot {
    width: 22px;
    height: 22px;
    border-radius: 50%;
    background: var(--brand-blue);
  }
  .brand__name {
    font-weight: 700;
    font-size: 27px;
    color: var(--brand-grey);
    letter-spacing: 0.2px;
  }
  .back__web {
    position: absolute;
    left: 0;
    right: 0;
    top: 206px;
    text-align: center;
    font-size: 12.5px;
    color: var(--ink);
  }
</style>
</head>
<body>
  <section class="card card--front" aria-label="Business card front">
    <div class="holder">
      <p class="holder__name">DARREL QUIMBY</p>
      <p class="holder__role">Pharmacy Manager</p>
    </div>
    <ul class="contact">
      <li>555 010 4477
        <svg viewBox="0 0 10 10" aria-hidden="true"><path d="M1 3.2C1 2 2.5 1.3 5 1.3S9 2 9 3.2V4H7V3.2H3V4H1z M2.2 8.7 3 5h4l.8 3.7z"/></svg>
      </li>
      <li>hello@willowbendpharmacy.example
        <svg viewBox="0 0 10 10" aria-hidden="true"><path d="M0.5 2h9v6h-9z M1.3 2.6 5 5.4 8.7 2.6" stroke="#7fb87a" stroke-width="0.8" fill="#fff"/></svg>
      </li>
      <li>www.willowbendpharmacy.example
        <svg viewBox="0 0 10 10" aria-hidden="true"><circle cx="5" cy="5" r="4.5"/></svg>
      </li>
    </ul>
  </section>

  <section class="card card--back" aria-label="Business card back">
    <div class="brand">
      <span class="brand__dot" aria-hidden="true"></span>
      <span class="brand__name">Willowbend Pharmacy</span>
    </div>
    <p class="back__web">www.willowbendpharmacy.example</p>
  </section>
</body>
</html>
```